依頼詳細
http://mirokan.jp/
こちらのコーポレーションサイトのデザイン追加と修正をお願いいたします。

①トップで使用している街並みの写真(東京の写真)を
東京以外の街並みでかっこいい雰囲気の写真に差し替えをお願いいたします。
青っぽい感じが希望ですが、雰囲気に合わせて今の色から変更していただいてOKです。
テキストの字体も雰囲気に合わせて変更していただいて大丈夫です。

②サイト内にある下記の項目をポップアップで表示させるようにしたいと思っており、その際に表示される各項目のデザイン作成をお願いいたします。
各項目ともテキストはそのままで、参考サイトのトップのように写真の上に文字があって、各事業の文字を大きく、説明は小さく入れてください。
写真・フィルターは①の雰囲気に合うようお任せいたします。
フィルターはあってもなくてもいいです。

・不動産仲介事業
・リフォームリノベーション事業
・注文住宅事業
・不動産コンサルティング

③右上に表示されている項目(Home・Service・Company・Contact)に
Greetingsを追加して下さい。
※代表挨拶の意味で追加したいのですが
ほかに良い表記がありましたらそちらでお願いいたします。

④conpanyの上に
③で追加したGreetingsの項目を追加してください。
※テキストはあとから入れたいので、文字のボリューム感がわかるように
テストのテキストを入れていただけると助かります。

⑤Companyの横に添付写真を入れられたらお願いいたします。
※こちらの写真は後ほど添付いたします。

参考サイト
https://palvestaworks.com/

何か説明など足りない点がございましたら
お手数ですが直接ご質問をお願いいたします。

よろしくお願いいたします。
サイトURL
http://mirokan.jp/
ページ数
1ページ
希望イメージ
シンプル 複雑
単色 カラフル
暗い 明るい
日常 高級
遊び心 厳粛
未来的 伝統的
女性的 男性的
希望する色
青系、水色系、無彩色系
納品ファイル
• イラストレーター形式 (.ai)
• フォトショップ形式 (.psd)
補足説明
company部分の写真の追加となります。
3枚添付していますので良さそうな写真でお願い致します。
※消毒のボトルなど、見栄え悪そうなものは加工していただいて構いません。

よろしくお願い致します。
申し訳ございません。
下記の項目の点を修正お願いいたします。

【修正前】
①トップで使用している街並みの写真(東京の写真)を

【修正後】
空、オフィス系や建築会社系、機械的デザイン等
いろんなパターンで見てみたいので
街並みと人間が入っていないものでお願いいたします。

よろしくお願いいたします。
■ 選んだ理由

弊社サイトに一番合っていたので当選とさせていただきました。

■ 提案者全員のお礼・コメント

ご参加ありがとうございました。

```html
<!DOCTYPE html>
<html lang="ja">
<head>
<meta charset="utf-8">
<title>株式会社Mirokan</title>
<link rel="stylesheet" href="https://fonts.googleapis.com/css2?family=Oswald:wght@500;600&family=Noto+Sans+JP:wght@400;500;700;900&display=swap">
<style>
:root{
  --ink:#222;
  --white:#fff;
  --accent:#1ea0e6;
  --teal:#5cc6c4;
  --dark:#2b2b2b;
  --light:#f3f3f3;
  --field:#eeeeee;
  --muted:#888;
}
*{margin:0;padding:0;box-sizing:border-box}
html,body{width:1200px;height:3048px;overflow:hidden;background:var(--white);font-family:"Noto Sans JP",sans-serif;color:var(--ink)}
.page{position:relative;width:1200px;height:3048px}
.section-title{font-family:"Oswald",sans-serif;font-weight:600;font-size:46px;letter-spacing:1px;line-height:1}
.section-title::after{content:"";display:block;width:80px;height:7px;background:var(--accent);margin-top:14px}
.center{text-align:center}
.center::after{margin-left:auto;margin-right:auto}

/* hero */
.hero{position:absolute;left:0;top:0;width:1200px;height:660px;background:linear-gradient(180deg,#c9d7e6 0%,#8fa8c2 45%,#5f7a98 100%)}
.brand{position:absolute;left:22px;top:30px;font-weight:900;font-size:26px;color:var(--ink)}
.nav{position:absolute;right:40px;top:48px;display:flex;gap:34px;font-family:"Oswald",sans-serif;font-weight:500;font-size:17px;color:var(--ink)}
.hero-copy{position:absolute;left:220px;top:200px;display:flex;flex-direction:column;align-items:flex-start;gap:16px}
.hero-copy span{display:inline-block;background:rgba(255,255,255,.82);font-weight:900;font-size:48px;line-height:1.2;padding:4px 14px;letter-spacing:2px}
.hero-copy .lead{margin-left:110px;font-size:54px}

/* service */
.service{position:absolute;left:0;top:660px;width:1200px;height:592px}
.service .section-title{position:absolute;left:0;right:0;top:60px}
.cards{position:absolute;left:100px;top:200px;display:flex;gap:40px}
.card{position:relative;width:220px;height:328px;background:linear-gradient(160deg,#7c9fcd 0%,#4d6f9f 60%,#3b567e 100%);color:var(--white);padding:16px 14px;box-shadow:0 4px 10px rgba(0,0,0,.15)}
.card svg{display:block;margin:0 auto 8px}
.card h3{font-size:22px;font-weight:700;line-height:1.25;margin-bottom:10px}
.card p{font-size:12px;line-height:1.7}

/* greeting */
.greeting{position:absolute;left:0;top:1252px;width:1200px;height:568px;background:var(--dark);color:var(--white)}
.greeting .section-title{position:absolute;left:0;right:0;top:60px}
.greeting-text{position:absolute;left:200px;top:152px;width:400px;font-size:13px;line-height:2;letter-spacing:.5px}
.greeting-photo{position:absolute;left:640px;top:152px;width:360px;height:292px;background:var(--white)}

/* company */
.company{position:absolute;left:0;top:1820px;width:1200px;height:600px;background:var(--light)}
.company .section-title{position:absolute;left:200px;top:40px}
.company-table{position:absolute;left:200px;top:168px;width:300px;font-size:11px;border-collapse:collapse}
.company-table th{text-align:left;font-weight:500;width:76px;padding:5px 0;vertical-align:top}
.company-table td{padding:5px 0;line-height:1.5}
.deco-grey{position:absolute;left:700px;top:80px;width:400px;height:420px;background:#9a9a9a}
.deco-teal{position:absolute;left:500px;top:150px;width:380px;height:440px;background:var(--teal)}
.company-photo{position:absolute;left:540px;top:110px;width:500px;height:330px;background:linear-gradient(135deg,#d8d4cc 0%,#a59d90 45%,#5d5a56 100%)}

/* contact */
.contact{position:absolute;left:0;top:2420px;width:1200px;height:628px}
.contact .section-title{position:absolute;left:0;right:0;top:52px}
.field{position:absolute;left:240px;width:680px;height:30px;background:var(--field);font-size:12px;color:var(--muted);padding:7px 12px}
.field.area{height:160px}
.submit{position:absolute;left:532px;top:488px;width:96px;height:36px;background:var(--accent);color:var(--white);font-size:14px;display:flex;align-items:center;justify-content:center}
</style>
</head>
<body>
<div class="page">

  <header class="hero" role="img" aria-label="青みがかった空とビルのメインビジュアル">
    <div class="brand">株式会社Mirokan</div>
    <nav class="nav"><span>Home</span><span>Service</span><span>Company</span><span>Contact</span><span>Greetings</span></nav>
    <div class="hero-copy">
      <span class="lead">ひとりひとりが</span>
      <span>マイホームの購入を検討している</span>
      <span>お客様の立場に寄り添い寄り添い、</span>
      <span>親身になったご提案をいたします。</span>
    </div>
  </header>

  <section class="service">
    <h2 class="section-title center">Service</h2>
    <div class="cards">
      <article class="card">
        <svg width="40" height="40" viewBox="0 0 40 40" fill="#fff"><circle cx="20" cy="13" r="7"/><path d="M6 36c0-8 6-13 14-13s14 5 14 13z"/></svg>
        <h3>不動産仲介事業</h3>
        <p>物件探しから契約・お引渡しまで、お客様の条件に合わせて丁寧にサポートいたします。地域の情報を活かし、安心できる住まい選びをお手伝いします。</p>
      </article>
      <article class="card">
        <svg width="40" height="40" viewBox="0 0 40 40" fill="#fff"><circle cx="15" cy="15" r="8"/><circle cx="15" cy="15" r="3" fill="#4d6f9f"/><circle cx="29" cy="27" r="6"/><circle cx="29" cy="27" r="2" fill="#4d6f9f"/></svg>
        <h3>リフォーム<br>リノベーション事業</h3>
        <p>住まいの不便や老朽化に合わせ、暮らしを見直すご提案を行います。小さな修繕から全面改装まで幅広く対応します。</p>
      </article>
      <article class="card">
        <svg width="40" height="40" viewBox="0 0 40 40" fill="#fff"><path d="M20 5 4 19h5v15h9v-9h4v9h9V19h5z"/></svg>
        <h3>注文住宅事業</h3>
        <p>ご家族の想いを形にする家づくりを、設計から施工まで一貫してご提案いたします。理想の暮らしを一緒に考えます。</p>
      </article>
      <article class="card">
        <svg width="40" height="40" viewBox="0 0 40 40" fill="#fff"><rect x="6" y="22" width="6" height="12"/><rect x="17" y="14" width="6" height="20"/><rect x="28" y="7" width="6" height="27"/></svg>
        <h3>不動産<br>コンサルティング</h3>
        <p>資産活用や売却、相続に関するご相談まで、専門知識をもとに最適な方法をご提案いたします。</p>
      </article>
    </div>
  </section>

  <section class="greeting">
    <h2 class="section-title center">Greeting</h2>
    <div class="greeting-text">ここに代表挨拶の文章が入ります。ここに代表挨拶の文章が入ります。ここに代表挨拶の文章が入ります。ここに代表挨拶の文章が入ります。ここに代表挨拶の文章が入ります。ここに代表挨拶の文章が入ります。ここに代表挨拶の文章が入ります。ここに代表挨拶の文章が入ります。ここに代表挨拶の文章が入ります。ここに代表挨拶の文章が入ります。</div>
    <div class="greeting-photo" role="img" aria-label="代表者写真の配置スペース"></div>
  </section>

  <section class="company">
    <h2 class="section-title">Company</h2>
    <table class="company-table">
      <tr><th>会社名</th><td>株式会社Mirokan</td></tr>
      <tr><th>所在地</th><td>東京都青葉区北町2-14-8 ミロカンビル3F</td></tr>
      <tr><th>電話番号</th><td>03-0000-1234</td></tr>
      <tr><th>代表者</th><td>代表 三浦</td></tr>
      <tr><th>設立</th><td>2015年4月</td></tr>
      <tr><th>資本金</th><td>1,000万円</td></tr>
      <tr><th>事業内容</th><td>不動産仲介事業<br>リフォーム事業<br>注文住宅事業</td></tr>
    </table>
    <div class="deco-grey"></div>
    <div class="deco-teal"></div>
    <div class="company-photo" role="img" aria-label="木目のデスクが並ぶオフィス内観の写真"></div>
  </section>

  <section class="contact">
    <h2 class="section-title center">Contact</h2>
    <div class="field" style="top:148px">お名前</div>
    <div class="field" style="top:200px">メールアドレス</div>
    <div class="field" style="top:252px">電話番号</div>
    <div class="field area" style="top:304px">お問い合わせ内容</div>
    <div class="submit">送信</div>
  </section>

</div>
</body>
</html>
```